English and Spanish Language School Needs a Business Card

Need a business card design a startup company called Corvelle Language School. The company will offer English and Spanish conversational level courses designed to make the learner feel comfortable with grammar and vocabulary. We would like to see a logo with some colour that should communicate learning, growth.

Target Market(s)

Consumers and businesses

Industry/Entity Type

Education

Contact Information for Business Card

TBD

Font styles to use
Serif

Requirements
Must have
• Include the following
• Logo
• Name
• Title
• Cellphone Number
• Office Phone number
• Email address
• Office Address

```html
<!DOCTYPE html>
<html lang="en">
<head>
<meta charset="utf-8">
<title>Corvelle Language School – Business Card</title>
<link rel="stylesheet" href="https://fonts.googleapis.com/css2?family=Open+Sans:wght@400;600;700&display=swap">
<style>
  :root {
    --backdrop: #5e5e5e;
    --card-light: #ffffff;
    --card-dark: #404040;
    --brand-red: #c81f2b;
    --brand-teal: #0a9ea9;
    --ink: #333333;
    --ink-light: #ffffff;
  }
  * { margin: 0; padding: 0; box-sizing: border-box; }
  html, body {
    width: 1200px; height: 1200px; overflow: hidden;
    background: var(--backdrop);
    font-family: "Open Sans", Arial, sans-serif;
  }
  .card {
    position: absolute;
    width: 610px; height: 346px;
    border-radius: 16px;
    overflow: hidden;
  }
  .card--front { left: 297px; top: 223px; background: var(--card-light); }
  .card--back { left: 294px; top: 632px; background: var(--card-dark); }
  .card__band { position: absolute; left: 0; top: 0; width: 610px; height: 346px; }

  .brand-name {
    position: absolute;
    font-weight: 700;
    color: var(--brand-red);
    white-space: nowrap;
    display: flex; align-items: center; gap: 10px;
    letter-spacing: -0.5px;
  }
  .brand-name__dot {
    width: 14px; height: 14px; border-radius: 50%;
    background: var(--brand-teal);
  }
  .card--front .brand-name { left: 43px; top: 62px; font-size: 30px; }
  .card--back .brand-name { left: 0; width: 610px; top: 138px; font-size: 34px; justify-content: center; }

  .person {
    position: absolute; left: 40px; top: 206px; width: 200px;
    text-align: center;
  }
  .person__name { color: var(--brand-red); font-size: 22px; line-height: 30px; }
  .person__title { color: var(--ink); font-size: 16px; line-height: 22px; }

  .divider {
    position: absolute; left: 256px; top: 190px;
    width: 1.5px; height: 113px; background: var(--brand-teal);
  }
  .contact { position: absolute; left: 288px; top: 192px; list-style: none; }
  .contact__item {
    display: flex; align-items: flex-start; gap: 6px;
    color: var(--ink); font-size: 15px; line-height: 20.5px;
  }
  .contact__item--address { margin-top: 8px; }
  .contact__icon { width: 12px; height: 14px; margin-top: 3px; flex: none; }

  .website {
    position: absolute; left: 0; width: 610px; top: 278px;
    text-align: center; color: var(--ink-light); font-size: 15px;
  }
</style>
</head>
<body>

<section class="card card--front" aria-label="Business card front">
  <svg class="card__band" viewBox="0 0 610 346" aria-hidden="true">
    <polygon points="0,305 483,346 0,346" fill="var(--brand-teal)"/>
  </svg>
  <div class="brand-name">Corvelle Language School<span class="brand-name__dot"></span></div>

  <div class="person">
    <p class="person__name">Marlow Fenner</p>
    <p class="person__title">Managing Partner</p>
  </div>

  <div class="divider"></div>

  <ul class="contact">
    <li class="contact__item">
      <svg class="contact__icon" viewBox="0 0 12 14" aria-hidden="true"><rect x="2.5" y="1" width="7" height="12" rx="1.2" fill="none" stroke="var(--brand-teal)" stroke-width="1.4"/><rect x="5" y="10.5" width="2" height="1" fill="var(--brand-teal)"/></svg>
      <span>(00) 000-0000</span>
    </li>
    <li class="contact__item">
      <svg class="contact__icon" viewBox="0 0 12 14" aria-hidden="true"><path d="M1 6 Q6 2 11 6 L10 7.5 L8 7 L8 6 Q6 5 4 6 L4 7 L2 7.5 Z" fill="var(--brand-teal)"/><rect x="2.5" y="8" width="7" height="4" rx="1" fill="var(--brand-teal)"/><circle cx="6" cy="10" r="1" fill="#fff"/></svg>
      <span>(00) 000-0000</span>
    </li>
    <li class="contact__item">
      <svg class="contact__icon" viewBox="0 0 12 14" aria-hidden="true"><rect x="1" y="4" width="10" height="7" fill="var(--brand-teal)"/><path d="M1 4 L6 8 L11 4" fill="none" stroke="#fff" stroke-width="1"/></svg>
      <span>mfenner@corvellelangsc.com</span>
    </li>
    <li class="contact__item contact__item--address">
      <svg class="contact__icon" viewBox="0 0 12 14" aria-hidden="true"><path d="M6 13.5 C3 9.5 1.5 7.5 1.5 5.5 A4.5 4.5 0 0 1 10.5 5.5 C10.5 7.5 9 9.5 6 13.5 Z" fill="var(--brand-teal)"/><circle cx="6" cy="5.5" r="1.8" fill="#fff"/></svg>
      <span>2240 Alder Cove Lane<br>Harwick, ME 04120</span>
    </li>
  </ul>
</section>

<section class="card card--back" aria-label="Business card back">
  <svg class="card__band" viewBox="0 0 610 346" aria-hidden="true">
    <polygon points="130,346 610,304 610,346" fill="var(--brand-red)"/>
  </svg>
  <div class="brand-name">Corvelle Language School<span class="brand-name__dot"></span></div>
  <p class="website">www.corvellelangsc.com</p>
</section>

</body>
</html>
```